Sehr schnelle und professionelle Abwicklung. Der Designer hat mir sogar einen Fehler im Buchrücken-Text gefunden. Ich bin sehr zufrieden und kann ihn uneingeschränkt weiter empfehlen.
Zielgruppe
Wir schreiben ebooks und haben verschiedene Zielgruppen. In diesem Projekt sind es Scherheitsbewusste Eigenheimbesitzer, welche sich über die aktiven und passiven Möglichkeiten zum Einbruchschutz informieren möchten
Aufgabenstellung
Es ist ein Tatgeber zur Vermeidung von Einbrüchen. Dem Design für unser Cover sind keine Grenzen gesetzt. Es soll ansprechend sein, und Lust auf mehr Content machen.

```html
<!DOCTYPE html>
<html lang="de">
<head>
<meta charset="utf-8">
<title>Einbruchschutz – Umschlagvarianten</title>
<link rel="stylesheet" href="https://fonts.googleapis.com/css2?family=Open+Sans:wght@400;600;700&display=swap">
<style>
  :root {
    --magenta: #cc007f;
    --slate: #6e6f80;
    --night: #15203a;
    --night-deep: #0c1424;
    --badge-dark: #35383c;
    --white: #ffffff;
    --rule: #9a9a9a;
    --page: #ffffff;
  }
  * { box-sizing: border-box; margin: 0; padding: 0; }
  html, body { width: 1200px; height: 2222px; overflow: hidden; background: var(--page); }
  body { position: relative; font-family: "Open Sans", Arial, sans-serif; color: var(--white); }

  .cover-wrap {
    position: absolute;
    width: 797px;
    height: 569px;
    box-shadow: 0 0 2px rgba(0,0,0,.25);
  }
  .cover-wrap--magenta { left: 207px; top: 140px; --back: var(--magenta); --badge: var(--badge-dark); }
  .cover-wrap--slate { left: 211px; top: 1166px; --back: var(--slate); --badge: var(--magenta); }

  .back-cover {
    position: absolute; left: 0; top: 0; width: 417px; height: 569px;
    background: var(--back);
  }
  .back-cover__publisher {
    position: absolute; left: 0; width: 386px; top: 24px;
    text-align: center; font-size: 9.5px; font-weight: 600;
  }
  .back-cover__title {
    position: absolute; left: 0; width: 386px; top: 120px;
    text-align: center;
  }
  .back-cover__kicker { font-size: 17px; font-weight: 600; line-height: 22px; }
  .back-cover__headline { font-size: 42px; font-weight: 700; line-height: 39px; letter-spacing: 1px; }
  .back-cover__subline { font-size: 12.5px; line-height: 20px; margin-top: 2px; }
  .back-cover__blurb {
    position: absolute; left: 65px; width: 256px; top: 286px;
    text-align: center; font-size: 8px; line-height: 12.3px;
  }
  .back-cover__web {
    position: absolute; left: 41px; top: 526px;
    font-size: 9px; font-weight: 600;
  }

  .spine-text {
    position: absolute; left: 399px; transform: translate(-50%, -50%) rotate(-90deg);
    white-space: nowrap;
  }
  .spine-text--title { top: 404px; font-size: 14.5px; font-weight: 600; }
  .spine-text--title strong { font-weight: 700; }
  .spine-text--publisher { top: 77px; font-size: 8px; }

  .front-cover {
    position: absolute; left: 417px; top: 0; width: 380px; height: 569px;
    overflow: hidden;
  }
  .front-cover__photo {
    position: absolute; inset: 0;
    background:
      radial-gradient(ellipse 45% 30% at 62% 35%, rgba(150,160,175,.55), transparent 70%),
      radial-gradient(ellipse 40% 14% at 55% 13%, rgba(205,170,150,.45), transparent 70%),
      radial-gradient(ellipse 40% 12% at 50% 88%, rgba(200,160,140,.35), transparent 70%),
      linear-gradient(180deg, var(--night) 0%, #1d2a44 50%, var(--night-deep) 100%);
  }
  .front-cover__kicker {
    position: absolute; left: 20px; top: 248px; height: 21px; padding: 0 13px 0 12px;
    background: var(--magenta); font-size: 18px; font-weight: 600; line-height: 21px;
  }
  .front-cover__headline {
    position: absolute; left: 30px; top: 280px;
    font-size: 53px; font-weight: 700; line-height: 48px; letter-spacing: 1.5px;
  }
  .front-cover__badge {
    position: absolute; left: 245px; top: 355px; width: 108px; height: 108px;
    border-radius: 50%; background: var(--badge);
    display: flex; flex-direction: column; align-items: center; justify-content: center;
    text-align: center; font-size: 11px; font-weight: 600; line-height: 14px;
  }
  .front-cover__badge::before, .front-cover__badge::after {
    content: ""; display: block; width: 40px; height: 1px; background: var(--white);
  }
  .front-cover__badge::before { margin-bottom: 9px; }
  .front-cover__badge::after { margin-top: 9px; }
  .front-cover__publisher {
    position: absolute; left: 0; width: 396px; top: 536px;
    text-align: center; font-size: 9.5px; font-weight: 600;
  }

  .divider {
    position: absolute; height: 0; border-top: 1px dotted var(--rule);
  }
  .divider--first { left: 206px; width: 802px; top: 992px; }
  .divider--second { left: 211px; width: 792px; top: 2033px; }
</style>
</head>
<body>

<section class="cover-wrap cover-wrap--magenta">
  <div class="back-cover">
    <p class="back-cover__publisher">Platzhalter Autor/Verlag</p>
    <div class="back-cover__title">
      <p class="back-cover__kicker">Aktiver &amp; passiver</p>
      <h2 class="back-cover__headline">EINBRUCH-<br>SCHUTZ</h2>
      <p class="back-cover__subline">Ratgeber zur Vermeidung von Einbrüchen</p>
    </div>
    <p class="back-cover__blurb">Illati repe eiur arupti bernam idigent. Nihici odiscipsum non res et ut ea ipsam, quiassim qui voloratis aut aut rendunt. Hiliqui dollorrum quis maios ium ulpa dionsequo expliquas adit od et re, volendaectia cor re cus acerspi stenim verisquam consed molorem pererum explige necupientur, nia nectore, vel molores min pla quas dolupta ecaborero to tem venis escium a vendis mi, ommolup tatiis ut re pligeni hiliquatur?</p>
    <p class="back-cover__web">www.platzhalter-text.de</p>
    <p class="spine-text spine-text--publisher">Platzhalter Autor/Verlag</p>
    <p class="spine-text spine-text--title">Aktiver &amp; passiver <strong>EINBRUCHSCHUTZ</strong></p>
  </div>
  <div class="front-cover">
    <div class="front-cover__photo" role="img" aria-label="Foto: Hände im Anzug schützen ein Haussymbol von oben und unten"></div>
    <p class="front-cover__kicker">Aktiver &amp; passiver</p>
    <h1 class="front-cover__headline">EINBRUCH-<br>SCHUTZ</h1>
    <p class="front-cover__badge">Der Ratgeber für<br>sicherheitsbewußte<br>Eigenheimbesitzer</p>
    <p class="front-cover__publisher">Platzhalter Autor/Verlag</p>
  </div>
</section>

<div class="divider divider--first"></div>

<section class="cover-wrap cover-wrap--slate">
  <div class="back-cover">
    <p class="back-cover__publisher">Platzhalter Autor/Verlag</p>
    <div class="back-cover__title">
      <p class="back-cover__kicker">Aktiver &amp; passiver</p>
      <h2 class="back-cover__headline">EINBRUCH-<br>SCHUTZ</h2>
      <p class="back-cover__subline">Ratgeber zur Vermeidung von Einbrüchen</p>
    </div>
    <p class="back-cover__blurb">Illati repe eiur arupti bernam idigent. Nihici odiscipsum non res et ut ea ipsam, quiassim qui voloratis aut aut rendunt. Hiliqui dollorrum quis maios ium ulpa dionsequo expliquas adit od et re, volendaectia cor re cus acerspi stenim verisquam consed molorem pererum explige necupientur, nia nectore, vel molores min pla quas dolupta ecaborero to tem venis escium a vendis mi, ommolup tatiis ut re pligeni hiliquatur?</p>
    <p class="back-cover__web">www.platzhalter-text.de</p>
    <p class="spine-text spine-text--publisher">Platzhalter Autor/Verlag</p>
    <p class="spine-text spine-text--title">Aktiver &amp; passiver <strong>EINBRUCHSCHUTZ</strong></p>
  </div>
  <div class="front-cover">
    <div class="front-cover__photo" role="img" aria-label="Foto: Hände im Anzug schützen ein Haussymbol von oben und unten"></div>
    <p class="front-cover__kicker">Aktiver &amp; passiver</p>
    <h1 class="front-cover__headline">EINBRUCH-<br>SCHUTZ</h1>
    <p class="front-cover__badge">Der Ratgeber für<br>sicherheitsbewußte<br>Eigenheimbesitzer</p>
    <p class="front-cover__publisher">Platzhalter Autor/Verlag</p>
  </div>
</section>

<div class="divider divider--second"></div>

</body>
</html>
```